Funding your Foodie Dreams!

I need a website design for a crowdfunding site that is 100% food/beverage oriented. Artbazaar is a crowdsourcing site and my site will be a crowdfunding site. It needs to be very clean, modern, BUT easy to use with a clear path to all critical elements.

This is the current site, that I need to fit into, http://www.grantygrove.com.hosted.pledgehostnode.com

This site, http://tinmeadow.co, is PERFECT in the fact that it does not look bland or corporate in anyway and it is beautiful and effective. My site is comparable to their "Fund" section. The photo's and ease of the site is what I would love to emulate, but my site needs to be more vibrant, fun, a happy place, which can be done with colors and textures of the site. Think of food, family, local restaurants, how you feel when you are there. I would love to have that feel just from a website.

*** These sites are some sites for competitor companies and how this site needs to operate.
boostwagon.com
mealrise.com
pledgorix.com
cashtopia.com

Here are a couple sites, that I like the look of:
us.vex.com
hopquill.com
505ladlepages.com

I would like to function like a Boostwagon but would love it to NOT look like all the rest.
Updates

I wanted to share this site, I found today.  Love the ease of the site and the look at feel but would want mine to me more fun, food, not as ... serious... but just as professional.

http://tinmeadow.co

Reason: Hello I am extending the deadline as I have yet to receive any viable designs but received some today that with some work might be the ones so please send any designs through and please send changes through quickly. I AM expecting to award this project but with the limited # of designs, might cancel it and re-issue for a far less $ amount but make it guaranteed. Thank you very much for the few designs that have been submitted to date. C

Target Market(s)

Technically savy individuals that have an entrepreneurial spirit. Individuals that will be reaching out to friends and family to use this site who will NOT be as technologically advanced and needs the site to be very clear and easy to use but not childish.

Industry/Entity Type

Crowdfunding

Font styles to use
Sans Serif

Colors
f04950
9bcb3c
ffffff
f37123
6b449b
0555a3

Requirements
Must have
• This website will be done using a white-lable platform and so I need someone that understands the limitations of that type of a platform and can work within those boundaries.

Pages Required:
Start a Campaign
Browse Campaigns
What is grantygrove?
Help
Contact

Header & Footer

Links to Social Media
Chatterbook
Chirplet
Snapvane
Clipboardly
Rambloo
Nice to have
• If you can provide any coding or direction for the coding of the design in HTML, Javascript and/or CSS, these designs will have preference.

Looking for a site that will grow from only crowdfunding to include a shopping component as well as section for campaign creators to be able to get help from service providers with their campaigns maybe a blog and a forum.
Should not have
• Do NOT provide canned websites that do not meet the Must Have's. I have to use the platform format as mentioned above as I am not have a 100% custom site developed. If these sites are provided they will be eliminated immediately.

Should not resemble a corporate site in anyway.

```html
<!DOCTYPE html>
<html lang="en">
<head>
<meta charset="utf-8">
<title>grantygrove – Funding your Foodie Dreams</title>
<link rel="stylesheet" href="https://fonts.googleapis.com/css2?family=Open+Sans:wght@400;600;700&display=swap">
<style>
:root{
  --red:#e4474d;
  --orange:#f37123;
  --purple:#6b449b;
  --blue:#0555a3;
  --green:#9bcb3c;
  --ink:#3a3a3a;
  --muted:#777;
  --line:#e3e3e3;
  --footer:#2c2c2c;
  --footer-deep:#232323;
  --white:#fff;
}
*{box-sizing:border-box;margin:0;padding:0}
html,body{width:669px;height:1200px;overflow:hidden;background:var(--white)}
body{position:relative;font-family:"Open Sans",Arial,sans-serif;color:var(--ink);font-size:8px;line-height:1.45}
a{color:inherit;text-decoration:none}
.abs{position:absolute}

/* header */
.brand{left:14px;top:14px;display:flex;align-items:center;gap:7px;font-size:24px;font-weight:700;color:var(--red);letter-spacing:-.5px}
.brand-dot{width:18px;height:18px;border-radius:50%;background:var(--red)}
.account{right:44px;top:14px;font-size:9px;color:var(--red);font-weight:600;letter-spacing:.3px}
.account span{margin:0 7px;color:#bbb}
.nav{left:319px;top:38px;display:flex;align-items:center;gap:20px;font-size:9.5px;color:#555}
.nav .cta{background:var(--purple);color:var(--white);padding:4px 12px;border-radius:2px;font-weight:600}

/* hero */
.hero{left:45px;top:68px;width:575px;height:267px;background:linear-gradient(135deg,#cfe3c1 0%,#9cc7d8 40%,#e7a9a7 75%,#f2d6b8 100%)}
.hero-caption{left:45px;top:279px;background:rgba(30,30,30,.78);color:var(--white);font-size:13px;font-weight:700;padding:6px 14px;letter-spacing:.2px}
.hero-dots{right:56px;top:314px;display:flex;gap:4px}
.hero-dots i{width:5px;height:5px;border-radius:50%;background:rgba(255,255,255,.6)}
.hero-dots i:first-child{background:var(--white)}

/* headings */
.section-title{font-size:10px;font-weight:700;color:var(--red);letter-spacing:.2px}

/* welcome */
.welcome{left:45px;top:348px;width:375px}
.welcome p{color:#555;font-size:7.6px;margin-top:6px}
.video{left:428px;top:379px;width:192px;height:101px;background:linear-gradient(135deg,#3a3a3a,#6e5a4a 60%,#2a2a2a);border-radius:2px}
.play{left:511px;top:415px;width:28px;height:28px;border-radius:50%;background:rgba(255,255,255,.85)}

/* campaigns */
.popular{left:45px;top:500px}
.card{top:531px;width:174px;height:272px;border:1px solid var(--line);background:var(--white)}
.card .photo{margin:4px;height:72px;background:linear-gradient(135deg,#8a6a4e,#c89a6a 50%,#5b6b4a)}
.card .title{margin:14px 8px 0;font-size:9px;color:var(--orange)}
.card .place{margin:8px 8px 0;font-size:7.5px;color:var(--muted);display:flex;align-items:center;gap:4px}
.card .desc{margin:8px 8px 0;font-size:7.5px;color:#555}
.card .rule{margin:24px 8px 0;border-top:1px solid var(--line)}
.card .stats{margin:8px 8px 0;display:flex;justify-content:space-between;font-size:7.5px;font-weight:700;color:#555;letter-spacing:.4px}
.card .bar{margin:6px 8px 0;height:4px;background:#e7e7e7;border-radius:2px}
.card .bar i{display:block;height:100%;width:42%;background:var(--red);border-radius:2px}

/* testimonials */
.testimonials{left:45px;top:843px;width:390px;height:149px;border:1px solid var(--line)}
.testimonials h3{text-align:center;font-size:11px;font-weight:600;margin-top:10px;color:#444}
.testimonials .quote{margin:8px 48px 0;font-size:7.5px;color:#666}
.qmark{font-size:26px;color:#bbb;font-family:Georgia,serif;line-height:1}
.author{left:20px;top:96px;display:flex;align-items:center;gap:8px}
.author .avatar{width:28px;height:28px;border-radius:50%;background:#b9a28c}
.author b{display:block;font-size:8px;color:#444}
.author span{font-size:7px;color:var(--blue)}
.t-dots{right:16px;top:118px;display:flex;gap:3px}
.t-dots i{width:4px;height:4px;border-radius:50%;background:#bbb}

/* social widget */
.likebox{left:455px;top:843px;width:165px;height:149px;border:1px solid var(--line);padding:8px}
.likebox .head{display:flex;gap:6px;align-items:center}
.likebox .sq{width:26px;height:26px;background:var(--red)}
.likebox .head b{font-size:8px;color:#333}
.likebox .count{font-size:7px;color:#555;margin-top:8px}
.faces{display:grid;grid-template-columns:repeat(6,20px);gap:3px;margin-top:5px}
.faces i{height:20px;background:#c7b5a3}
.faces i:nth-child(3n){background:#a9b8c6}
.faces i:nth-child(4n){background:#d3c09a}
.likebox .plugin{font-size:6.5px;color:#888;margin-top:6px}

/* footer */
.footer{left:0;top:1015px;width:669px;height:185px;background:var(--footer);color:#bbb}
.f-col{top:1035px}
.f-col h4{font-size:8.5px;color:var(--white);font-weight:700;margin-bottom:8px}
.f-col li{list-style:none;font-size:7.5px;line-height:14px}
.socials{display:flex;gap:6px}
.socials i{width:16px;height:16px;border-radius:2px}
.start-btn{display:inline-block;background:#4a4a4a;color:var(--white);font-size:8.5px;font-weight:700;padding:6px 18px;letter-spacing:.5px;border-radius:2px}
.f-rule{left:0;top:1158px;width:669px;border-top:1px solid #3d3d3d}
.copyright{left:45px;top:1170px;font-size:7.5px;color:#aaa}
.to-top{right:45px;top:1170px;font-size:7.5px;color:#aaa}
</style>
</head>
<body>

<header>
  <a class="brand abs" href="#"><span class="brand-dot"></span>grantygrove</a>
  <div class="account abs"><a href="#">LOGIN</a><span>|</span><a href="#">CREATE ACCOUNT</a></div>
  <nav class="nav abs">
    <a class="cta" href="#">Start a Campaign</a>
    <a href="#">Browse</a>
    <a href="#">Contact Us</a>
    <a href="#">About Us</a>
    <a href="#">Help</a>
  </nav>
</header>

<section>
  <div class="hero abs" role="img" aria-label="Photo of three smiling children outdoors"></div>
  <h1 class="hero-caption abs">WELCOME TO YOUR NEW CROWD FUNDING PLATFORM</h1>
  <div class="hero-dots abs"><i></i><i></i><i></i><i></i></div>
</section>

<section class="welcome abs">
  <h2 class="section-title">WELCOME TO OUR WEBSITE</h2>
  <p>Duis autem vel eum iriure dolor in hendrerit in vulputate velit esse molestie consequat, vel illum dolore eu feugiat nulla facilisi. Typi non habent claritatem.</p>
  <p>Duis autem vel eum iriure dolor in hendrerit in vulputate velit esse molestie consequat, vel illum dolore eu feugiat nulla facilisis at vero eros et accumsan et iusto odio dignissim qui blandit praesent luptatum zzril delenit augue duis dolore te feugait nulla facilisi. Nam liber tempor cum soluta nobis eleifend option congue nihil imperdiet doming id quod mazim placerat facer possim assum. Typi non habent claritatem insitam; est usus legentis in iis qui facit eorum claritatem.</p>
</section>
<div class="video abs" role="img" aria-label="Video still of a kitchen scene"></div>
<svg class="play abs" viewBox="0 0 28 28"><circle cx="14" cy="14" r="14" fill="none"/><path d="M11 8.5 L20 14 L11 19.5Z" fill="#333"/></svg>

<h2 class="section-title popular abs">MOST POPULAR CAMPAIGNS</h2>

<article class="card abs" style="left:45px">
  <div class="photo" role="img" aria-label="Photo of a campaign dish"></div>
  <h3 class="title">Nam liber tempor cum soluta nobis</h3>
  <div class="place"><svg width="7" height="9" viewBox="0 0 7 9"><path d="M3.5 0A3.5 3.5 0 0 0 0 3.5C0 6 3.5 9 3.5 9S7 6 7 3.5A3.5 3.5 0 0 0 3.5 0Z" fill="#999"/><circle cx="3.5" cy="3.5" r="1.2" fill="#fff"/></svg>Krisal Gam Cu</div>
  <p class="desc">Join us in funding a new political party dedicated to promoting and encouraging Australian arts and creativity!</p>
  <div class="rule"></div>
  <div class="stats"><span>$13,445USD</span><span>19 DAYS LEFT</span></div>
  <div class="bar"><i></i></div>
</article>

<article class="card abs" style="left:246px">
  <div class="photo" role="img" aria-label="Photo of a crowd at a food event" style="background:linear-gradient(135deg,#6b7d8c,#b59a7a 50%,#4d5a4a)"></div>
  <h3 class="title">Nam liber tempor cum soluta nobis</h3>
  <div class="place"><svg width="7" height="9" viewBox="0 0 7 9"><path d="M3.5 0A3.5 3.5 0 0 0 0 3.5C0 6 3.5 9 3.5 9S7 6 7 3.5A3.5 3.5 0 0 0 3.5 0Z" fill="#999"/><circle cx="3.5" cy="3.5" r="1.2" fill="#fff"/></svg>Krisal Gam Cu</div>
  <p class="desc">Join us in funding a new political party dedicated to promoting and encouraging Australian arts and creativity!</p>
  <div class="rule"></div>
  <div class="stats"><span>$13,445USD</span><span>19 DAYS LEFT</span></div>
  <div class="bar"><i></i></div>
</article>

<article class="card abs" style="left:446px">
  <div class="photo" role="img" aria-label="Photo of a crowd at a market" style="background:linear-gradient(135deg,#7a8a9a,#c2a684 50%,#5d6b5a)"></div>
  <h3 class="title">Nam liber tempor cum soluta nobis</h3>
  <div class="place"><svg width="7" height="9" viewBox="0 0 7 9"><path d="M3.5 0A3.5 3.5 0 0 0 0 3.5C0 6 3.5 9 3.5 9S7 6 7 3.5A3.5 3.5 0 0 0 3.5 0Z" fill="#999"/><circle cx="3.5" cy="3.5" r="1.2" fill="#fff"/></svg>Krisal Gam Cu</div>
  <p class="desc">Join us in funding a new political party dedicated to promoting and encouraging Australian arts and creativity!</p>
  <div class="rule"></div>
  <div class="stats"><span>$13,445USD</span><span>19 DAYS LEFT</span></div>
  <div class="bar"><i></i></div>
</article>

<section class="testimonials abs">
  <h3>Testimonials</h3>
  <span class="qmark abs" style="left:18px;top:32px">&ldquo;</span>
  <p class="quote">Nascetur et amet tincidunt elit. Pellentesque habitant senectus et netus malesuada fames ac turpis egestas. Nulla facilisi, pellentesque interdum mollis tristique. Duis autem vel eum iriure dolor. Typi non habent claritatem insitam; est usus.</p>
  <span class="qmark abs" style="right:18px;top:74px">&rdquo;</span>
  <div class="author abs">
    <div class="avatar" role="img" aria-label="Portrait of the reviewer"></div>
    <div><b>Marlow Teague</b><span>Company Name</span></div>
  </div>
  <div class="t-dots abs"><i></i><i></i><i></i><i></i></div>
</section>

<aside class="likebox abs">
  <div class="head"><span class="sq"></span><div><b>Granty Grove</b><div style="font-size:7px;color:#666">Like</div></div></div>
  <p class="count">20 people like Granty Grove</p>
  <div class="faces" role="img" aria-label="Profile photos of followers">
    <i></i><i></i><i></i><i></i><i></i><i></i>
    <i></i><i></i><i></i><i></i><i></i><i></i>
  </div>
  <p class="plugin">Chatterbook social plugin</p>
</aside>

<footer>
  <div class="footer abs"></div>
  <div class="f-col abs" style="left:45px">
    <h4>Browse Campaigns</h4>
    <ul><li>Featured Campaigns</li><li>Successful Campaigns</li><li>New Campaigns</li><li>Ending Soon</li><li>Most Funded Campaigns</li></ul>
  </div>
  <div class="f-col abs" style="left:194px">
    <h4>About</h4>
    <ul><li>About grantygrove</li><li>Contact Us</li><li>Help</li><li>Privacy Policy</li><li>Terms Of Service</li></ul>
  </div>
  <div class="f-col abs" style="left:323px">
    <h4>Follow us on</h4>
    <div class="socials">
      <i style="background:#3b5998" title="Chatterbook"></i>
      <i style="background:#2aa9e0" title="Chirplet"></i>
      <i style="background:var(--orange)" title="Rambloo"></i>
      <i style="background:var(--red)" title="Clipboardly"></i>
    </div>
  </div>
  <div class="f-col abs" style="left:480px">
    <h4>Ready to start?</h4>
    <a class="start-btn" href="#">START A CAMPAIGN</a>
  </div>
  <div class="f-rule abs"></div>
  <p class="copyright abs">Copyright ©2013. All Rights Reserved.</p>
  <a class="to-top abs" href="#">▲</a>
</footer>

</body>
</html>
```